Website Development for quillmarsh.com.au

Build a new Wordpress/Responsive website for quillmarsh.com.au

Target Market(s)

Compliance Managers, Risk Managers, Information Security and Cyber Security Professionals, Chief Data/Digital Officers, Chief Operating/Financial Officers, Business Continuity Professionals, Disaster Recovery Planners, Small Business Owners, Local/Federal Government entities

Industry/Entity Type

Data Service

Coding

Coded - Design and coding required

Number of Pages Required

5+ page

Font styles to use
Sans Serif

Colors

Designer to choose colors to be used in the design.

Requirements
Must have
• 1. Site Structure: Home Page plus the following chapter-pages for a) Services b) About c) Resources d) Blog e) Contact Us
• 2. Prefer site to built on wordpress and we can purchase a theme if needed (we currently use The7 for other sites)
• 3. Blog needs to be wordpress based
• 4. We will host the site ourselves on our own servers
• 5. Responsive Design
Nice to have
• 1. Livechat capability/interface
• 2. Capability for marketing automation integration (such as hubspot, marketo, infusionsoft etc)
• 3. Capability for CRM integration (Salesforce)

```html
<!DOCTYPE html>
<html lang="en">
<head>
<meta charset="utf-8">
<title>Quillmarsh — Making Your Data Accessible &amp; Actionable</title>
<link href="https://fonts.googleapis.com/css2?family=Poppins:wght@300;400;500;600&family=Raleway:wght@400;500;700&display=swap" rel="stylesheet">
<style>
:root{
  --blue:#1a6fc4;
  --blue-dark:#0d4f99;
  --navy:#06133a;
  --ink:#1c1c2a;
  --text:#4a4a55;
  --muted:#8a8a95;
  --blob:#eaf3fd;
  --blob-2:#f3f8fe;
  --line:#d8dde6;
  --white:#ffffff;
}
*{box-sizing:border-box;margin:0;padding:0}
html,body{width:1200px;height:3956px;overflow:hidden}
body{position:relative;background:var(--white);font-family:"Poppins",sans-serif;color:var(--text)}
.abs{position:absolute}
.heading{font-family:"Raleway",sans-serif;font-weight:400;color:var(--ink);font-size:33px}
.heading strong{color:var(--blue);font-weight:700}
.rule{width:52px;height:3px;background:var(--blue);margin-top:10px}
.btn{display:inline-flex;align-items:center;gap:14px;height:48px;padding:0 30px 0 6px;border-radius:24px;background:linear-gradient(90deg,var(--blue-dark),var(--blue));color:var(--white);font-size:14px;font-weight:500;box-shadow:0 8px 18px rgba(26,111,196,.35)}
.btn .dot{width:38px;height:38px;border-radius:50%;background:var(--navy)}

/* header */
.site-header{left:0;top:0;width:1200px;height:80px;background:var(--white)}
.brand{left:145px;top:18px;display:flex;align-items:center;gap:10px;font-size:26px;font-weight:600;color:var(--blue)}
.brand i{width:30px;height:30px;background:var(--blue);border-radius:4px;display:block}
.nav{right:140px;top:0;display:flex;height:80px}
.nav a{display:flex;align-items:center;padding:0 21px;font-size:12px;color:var(--ink);text-decoration:none;letter-spacing:.3px}
.nav a.active{color:var(--blue);border-bottom:3px solid var(--blue)}

/* hero */
.hero{left:0;top:80px;width:1200px;height:434px;background:radial-gradient(circle at 80% 40%,#1f67c9 0%,#0b2a72 35%,#050f33 75%)}
.hero-visual{left:640px;top:0;width:560px;height:434px;background:radial-gradient(circle at 45% 40%,rgba(80,200,255,.55),rgba(20,70,180,.15) 55%,transparent 70%)}
.hero-title{left:142px;top:120px;font-family:"Raleway",sans-serif;font-size:44px;line-height:54px;color:var(--white);font-weight:400}
.hero-title strong{font-weight:700}
.hero-sub{left:142px;top:232px;width:440px;font-size:12px;line-height:19px;color:#d6e2f5}
.hero .btn{position:absolute;left:142px;top:294px}

/* blobs */
.blobs{left:0;top:514px;width:1200px;height:3060px}

/* about */
.about-art{left:185px;top:712px;width:370px;height:318px;border-radius:16px;background:linear-gradient(160deg,#dbe8fb,#c6d8f4)}
.about-copy{left:633px;top:700px;width:425px}
.about-copy p{font-size:11.5px;line-height:19px;margin-top:16px}
.about-copy p a{color:var(--blue);text-decoration:none;font-weight:500}
.about-copy .cta{font-size:15px;line-height:25px;color:var(--ink);margin-top:24px}
.about-copy .cta strong{color:var(--blue);font-weight:600}

/* services */
.services{left:145px;top:1235px;width:400px}
.services .desc{font-size:11.5px;line-height:18px;margin-top:20px}
.service-list{left:145px;top:1415px;list-style:none}
.service-list li{display:flex;align-items:center;gap:22px;height:53px;margin-bottom:41px;font-size:19px;color:var(--ink)}
.shield{width:54px;height:54px;border-radius:50% 50% 50% 50%/40% 40% 60% 60%;background:var(--blue-dark);flex:none}
.services-btn{left:145px;top:1803px}
.services-art{left:607px;top:1424px;width:474px;height:316px;border-radius:14px;background:linear-gradient(160deg,#e9eef6,#d5e3f7)}

/* different */
.diff-art{left:92px;top:2017px;width:408px;height:383px;border-radius:45% 55% 50% 50%;background:linear-gradient(150deg,#dfeafc,#c8daf6)}
.diff{left:633px;top:2010px;width:440px}
.diff-list{left:633px;top:2095px;list-style:none;width:440px}
.diff-list li{display:flex;gap:20px;height:84px}
.diff-list .ico{width:44px;height:44px;flex:none}
.diff-list h3{font-size:15.5px;font-weight:500;color:var(--ink);line-height:22px}
.diff-list p{font-size:11px;line-height:17px}

/* team */
.team-head{left:0;top:2548px;width:1200px;text-align:center}
.team-head .rule{margin:10px auto 0}
.card{top:2690px;height:382px;background:var(--white);box-shadow:0 6px 24px rgba(20,50,110,.08);text-align:center;padding:34px 12px 0}
.card .photo{height:206px;border:2px solid #c9ccd2;background:linear-gradient(180deg,#c9ccd2,#8e97a5)}
.card .name{margin-top:18px;font-size:14px;color:var(--ink);letter-spacing:.5px}
.card .role{font-size:11px;color:var(--muted);margin-top:2px}
.card .social{display:flex;justify-content:center;gap:9px;margin-top:12px}
.card .social i{width:8px;height:8px;border-radius:50%;background:#777;display:block}
.card .frame{position:absolute;left:12px;right:12px;top:34px;bottom:32px;border:2px solid #c9ccd2;border-top:none;pointer-events:none}
.card.featured .name{color:var(--blue);font-weight:500}
.card.featured .frame{border-color:var(--blue);border-top:2px solid var(--blue)}
.arrow{top:2843px;width:36px;height:36px;border-radius:50%;background:var(--white);box-shadow:0 3px 12px rgba(0,0,0,.1)}

/* blog */
.blog-head{left:0;top:3166px;width:1200px;text-align:center}
.blog-head .rule{margin:10px auto 0}
.post{top:3275px;width:432px;height:201px;background:var(--white);box-shadow:0 6px 24px rgba(20,50,110,.1);display:flex}
.post .thumb{width:153px;height:201px;background:linear-gradient(160deg,#b7bfc9,#4b5564);flex:none}
.post .body{padding:20px 18px}
.post h3{font-size:14px;font-weight:500;color:var(--ink);line-height:21px}
.post .date{font-size:11px;color:var(--blue);margin-top:8px}
.post p{font-size:10.5px;line-height:16px;margin-top:10px}

/* footer */
.site-footer{left:0;top:3573px;width:1200px;height:383px;background:radial-gradient(ellipse at 50% 100%,#123a8c,#071a4f 55%,#040d30)}
.contact-row{left:0;top:3573px;width:1200px;height:110px;color:#c4d1ea}
.contact-item{position:absolute;top:40px;width:300px;text-align:center;font-size:11px;line-height:16px}
.contact-item svg{display:block;margin:0 auto 14px;height:22px}
.contact-line{position:absolute;top:51px;height:1px;background:rgba(255,255,255,.3)}
.foot-nav{left:0;top:3735px;width:1200px;display:flex;justify-content:center;gap:26px}
.foot-nav a{color:var(--white);font-size:13px;text-decoration:none}
.foot-btn{left:513px;top:3818px}
.foot-bottom{left:142px;top:3910px;width:916px;display:flex;align-items:center;justify-content:space-between;font-size:10.5px;color:#c4d1ea}
.foot-bottom .legal{margin-left:-90px}
.socials{display:flex;gap:10px}
.socials i{width:28px;height:28px;border-radius:50%;background:#1f4fa8;border:1px solid rgba(255,255,255,.5);display:block}
</style>
</head>
<body>

<header class="site-header abs">
  <div class="brand abs"><i></i>Quillmarsh</div>
  <nav class="nav abs">
    <a class="active" href="#">HOME</a><a href="#">ABOUT</a><a href="#">SERVICES</a><a href="#">RESOURCES</a><a href="#">BLOG</a><a href="#">CONTACT US</a>
  </nav>
</header>

<section class="hero abs">
  <div class="hero-visual abs" role="img" aria-label="Hands holding a glowing digital globe of data icons"></div>
  <h1 class="hero-title abs">Making Your <strong>Data</strong><br>Accessible &amp; Actionable</h1>
  <p class="hero-sub abs">Duis autem vel eum iriure dolor in hendrerit in vulputate velit esse molestie consequat, vel illum dolore eu feugiat nulla facilisi.</p>
  <span class="btn"><span class="dot"></span>Read More</span>
</section>

<svg class="blobs abs" viewBox="0 0 1200 3060" aria-hidden="true">
  <path d="M0 30 C180 -10 420 40 520 200 C620 360 640 540 580 680 C520 820 300 900 120 860 C60 850 20 840 0 830 Z" fill="var(--blob-2)"/>
  <path d="M1200 1240 C1000 1270 880 1400 860 1560 C840 1760 900 1960 1020 2090 C1100 2170 1160 2200 1200 2210 Z" fill="var(--blob-2)"/>
  <path d="M0 1760 C200 1800 320 1950 300 2150 C280 2300 160 2380 0 2400 Z" fill="var(--blob-2)"/>
  <path d="M0 2090 C300 2010 600 2030 800 2080 C980 2130 1120 2110 1200 2080 L1200 3060 L0 3060 Z" fill="var(--blob)" opacity=".55"/>
</svg>

<div class="about-art abs" role="img" aria-label="Illustration of people arranging charts on a large computer monitor"></div>
<section class="about-copy abs">
  <h2 class="heading">About <strong>Quillmarsh</strong></h2>
  <div class="rule"></div>
  <p><a href="#">Lorem ipsum dolor sit amet</a>, consectetuer adipiscing elit, sed diam nonummy nibh euismod tincidunt ut laoreet dolore magna aliquam erat volutpat. Ut wisi enim ad minim veniam, quis nostrud exerci tation ullamcorper suscipit lobortis nisl ut aliquip ex ea commodo consequat. Duis autem vel eum iriure dolor in hendrerit in vulputate velit esse molestie consequat, vel illum dolore eu feugiat nulla facilisis at vero eros et accumsan et iusto odio dignissim qui blandit praesent luptatum zzril delenit augue duis dolore te feugait nulla facilisi.</p>
  <p>Lorem ipsum dolor sit amet, consectetuer adipiscing elit, sed diam nonummy nibh euismod tincidunt ut laoreet dolore magna aliquam erat volutpat. Ut wisi enim ad minim veniam.</p>
  <p class="cta">Get the support you need now. <strong>Contact our 24/7 support line to get started.</strong></p>
</section>

<section class="services abs">
  <h2 class="heading">Our <strong>Services</strong></h2>
  <div class="rule"></div>
  <p class="desc">Quillmarsh is a long established fact that a reader will be distracted by the readable content of a page when looking at its layout. The point of using Lorem Ipsum is that it has a more-or-less normal distribution of letters</p>
</section>
<ul class="service-list abs">
  <li><span class="shield"></span>Data Resiliency</li>
  <li><span class="shield"></span>Data Management Services</li>
  <li><span class="shield"></span>Industry Solutions</li>
  <li><span class="shield"></span>Ransomware Protection</li>
</ul>
<span class="btn services-btn abs"><span class="dot"></span>Read More</span>
<div class="services-art abs" role="img" aria-label="Illustration of a man beside a browser window showing a padlock"></div>

<div class="diff-art abs" role="img" aria-label="Illustration of business people standing on a large smartphone"></div>
<section class="diff abs">
  <h2 class="heading">What Makes <strong>Us Different?</strong></h2>
  <div class="rule"></div>
</section>
<ul class="diff-list abs">
  <li><svg class="ico" viewBox="0 0 44 44"><circle cx="22" cy="22" r="16" fill="none" stroke="var(--blue)" stroke-width="2"/><path d="M14 26 l6-6 4 4 8-8" fill="none" stroke="var(--blue)" stroke-width="2"/></svg><div><h3>Business Strategy</h3><p>Quillmarsh is a long established fact that a reader will be distracted by the readable content.</p></div></li>
  <li><svg class="ico" viewBox="0 0 44 44"><circle cx="22" cy="22" r="16" fill="none" stroke="var(--blue)" stroke-width="2"/><circle cx="22" cy="20" r="6" fill="none" stroke="var(--blue)" stroke-width="2"/><path d="M19 30 h6" stroke="var(--blue)" stroke-width="2"/></svg><div><h3>Innovation</h3><p>Quillmarsh is a long established fact that a reader will be distracted by the readable content.</p></div></li>
  <li><svg class="ico" viewBox="0 0 44 44"><rect x="8" y="12" width="28" height="18" rx="2" fill="none" stroke="var(--blue)" stroke-width="2"/><path d="M16 34 h12" stroke="var(--blue)" stroke-width="2"/></svg><div><h3>Technology Adoption</h3><p>Quillmarsh is a long established fact that a reader will be distracted by the readable content.</p></div></li>
  <li><svg class="ico" viewBox="0 0 44 44"><circle cx="22" cy="22" r="16" fill="none" stroke="var(--blue)" stroke-width="2" stroke-dasharray="4 3"/><path d="M22 12 v10 l7 5" fill="none" stroke="var(--blue)" stroke-width="2"/></svg><div><h3>Agility &amp; Flexibility</h3><p>Quillmarsh is a long established fact that a reader will be distracted by the readable content.</p></div></li>
</ul>

<section class="team-head abs">
  <h2 class="heading">Our <strong>Team</strong></h2>
  <div class="rule"></div>
</section>
<span class="arrow abs" style="left:140px"></span>
<article class="card abs" style="left:190px;width:192px"><div class="photo" role="img" aria-label="Portrait photo of team member Rowan"></div><div class="name">ROWAN</div><div class="role">Designation Here</div><div class="social"><i></i><i></i><i></i><i></i></div><div class="frame"></div></article>
<article class="card featured abs" style="left:398px;width:180px"><div class="photo" role="img" aria-label="Portrait photo of team member Tessa Lyle"></div><div class="name">TESSA LYLE</div><div class="role">Designation Here</div><div class="social"><i></i><i></i><i></i><i></i></div><div class="frame"></div></article>
<article class="card abs" style="left:610px;width:188px"><div class="photo" role="img" aria-label="Portrait photo of team member Marcus Fenn"></div><div class="name">MARCUS FENN</div><div class="role">Designation Here</div><div class="social"><i></i><i></i><i></i><i></i></div><div class="frame"></div></article>
<article class="card abs" style="left:820px;width:190px"><div class="photo" role="img" aria-label="Portrait photo of team member Owen Parrish"></div><div class="name">OWEN PARRISH</div><div class="role">Designation Here</div><div class="social"><i></i><i></i><i></i><i></i></div><div class="frame"></div></article>
<span class="arrow abs" style="left:1022px"></span>

<section class="blog-head abs">
  <h2 class="heading">Latest <strong>Blog</strong></h2>
  <div class="rule"></div>
</section>
<article class="post abs" style="left:142px"><div class="thumb" role="img" aria-label="Photo of a businessman in a suit"></div><div class="body"><h3>Adipiscing Elit, Sed Diam Nonu Mmy Nibh Lorem Ipsum</h3><div class="date">15 Feb 2019</div><p>Adipiscing elit, sed diam nonu mmy nibh euismod tincidunt ut laoreet dolore magna aliquam erat</p></div></article>
<article class="post abs" style="left:625px"><div class="thumb" role="img" aria-label="Photo of colleagues in an office meeting"></div><div class="body"><h3>Adipiscing Elit, Sed Diam Nonu Mmy Nibh Lorem Ipsum</h3><div class="date">15 Feb 2019</div><p>Adipiscing elit, sed diam nonu mmy nibh euismod tincidunt ut laoreet dolore magna aliquam erat</p></div></article>

<footer class="site-footer abs"></footer>
<div class="contact-row abs">
  <span class="contact-line" style="left:378px;width:198px"></span>
  <span class="contact-line" style="left:624px;width:186px"></span>
  <div class="contact-item" style="left:206px"><svg width="16" height="22" viewBox="0 0 16 22"><path d="M8 1 C4 1 1 4 1 8 C1 13 8 21 8 21 C8 21 15 13 15 8 C15 4 12 1 8 1 Z" fill="none" stroke="#8fb3ec" stroke-width="1.5"/><circle cx="8" cy="8" r="2.5" fill="#8fb3ec"/></svg>12 Lorem ipsum dolor 456 Sed diam, nonummy</div>
  <div class="contact-item" style="left:450px"><svg width="20" height="20" viewBox="0 0 20 20"><path d="M4 2 l4 0 1 5 -2 2 c1 2 3 4 5 5 l2-2 5 1 0 4 c-8 1 -16 -7 -15 -15 Z" fill="none" stroke="#8fb3ec" stroke-width="1.5"/></svg>Phone: (00) 123 456 7890</div>
  <div class="contact-item" style="left:683px"><svg width="22" height="20" viewBox="0 0 22 20"><path d="M1 9 L21 1 L15 19 L10 12 Z M10 12 L21 1" fill="none" stroke="#8fb3ec" stroke-width="1.5"/></svg>Email: info@quillmarsh.com.au</div>
</div>
<nav class="foot-nav abs"><a href="#">Home</a><a href="#">About Us</a><a href="#">Services</a><a href="#">Resources</a><a href="#">Blog</a></nav>
<span class="btn foot-btn abs"><span class="dot"></span>Contact Us</span>
<div class="foot-bottom abs">
  <span>Copyright 2019 @ Quillmarsh. All Rights Reserved.</span>
  <span class="legal">Terms of services / Privacy Policy</span>
  <span class="socials"><i></i><i></i><i></i><i></i></span>
</div>

</body>
</html>
```